Leonard The Realtor Business Card Design

I need a new card design for my real estate business in Seattle Wa. I am interested in a unique design. My business revolves around my personal services and I want the card to show professionalism, creativity and good execution. I specialize in residential real estate in Capitol hill / downtown neighborhoods. The card is my first impression on may of my clients and in the service industry any time you can stand out from the crowd and make an impression will go a long way.

Target Market(s)

I will be handing the card to prospects/ potential buyers and sellers of residential real estate.

Industry/Entity Type

Real Estate Agent

Contact Information for Business Card

Email: Info@Leonardtherealtor.com Website: LeonardtheRealtor.com Cell phone: 206-555-0147 Fax 206-555-0193

Font styles to use
Sans Serif

Colors
0255a3
ffc214

Requirements
Must have
• I will need to have my firms logo "Harbor 9" and my logo "LTR" on the business card. I would like to have my firms logo smaller then mine. I would also like to have my photo on the card. By business colors are gold and white with blue accents.
Nice to have
• It would be nice to have a unique shape or feel (texture) rather then your standard business card. I saw cardmill press had metal cards which could be interesting.

```html
<!DOCTYPE html>
<html lang="en">
<head>
<meta charset="utf-8">
<title>Leonard The Realtor – Business Card</title>
<link rel="stylesheet" href="https://fonts.googleapis.com/css2?family=Open+Sans:wght@400;600&family=Roboto:wght@500;700&display=swap">
<style>
  :root {
    --gold: #856227;
    --silver-light: #f4f4f4;
    --silver-mid: #d6d6d8;
    --silver-dark: #b9b9bc;
    --ink: #333333;
    --ink-soft: #5c5c5c;
    --page: #ffffff;
  }
  * { box-sizing: border-box; margin: 0; padding: 0; }
  html, body { width: 1200px; height: 1126px; overflow: hidden; background: var(--page); }
  .canvas { position: relative; width: 1200px; height: 1126px; }

  .card {
    position: absolute; left: 150px; width: 900px; height: 514px;
    border-radius: 34px; overflow: hidden;
    box-shadow: 0 4px 14px rgba(0,0,0,.22);
  }
  .card--back { top: 30px; }
  .card--front { top: 582px; background: #fff; }

  .brushed {
    background:
      repeating-linear-gradient(0deg, rgba(255,255,255,.18) 0 1px, rgba(0,0,0,.03) 1px 3px),
      linear-gradient(90deg, var(--silver-dark) 0%, var(--silver-mid) 22%, var(--silver-light) 50%, var(--silver-mid) 78%, var(--silver-dark) 100%);
  }
  .card--back .brushed { position: absolute; inset: 0; }

  .wordmark {
    font-family: "Roboto", sans-serif; font-weight: 700; color: var(--gold);
    letter-spacing: .5px; white-space: nowrap; line-height: 1;
  }
  .card--back .wordmark {
    position: absolute; left: 0; right: 0; top: 214px; text-align: center; font-size: 64px;
  }

  .front-top { position: absolute; left: 0; top: 0; width: 100%; height: 234px; }
  .gold-rule { position: absolute; left: 0; width: 100%; height: 6px; background: var(--gold); }
  .gold-rule--band { top: 232px; }
  .gold-rule--foot { top: 484px; }
  .front-foot { position: absolute; left: 0; top: 490px; width: 100%; height: 24px; }

  .portrait {
    position: absolute; left: 60px; top: 66px; width: 270px; height: 270px;
    border: 6px solid var(--gold);
    background: linear-gradient(180deg, #d9d6d2 0%, #b9b3ad 45%, #2d3b5c 80%, #1f2b46 100%);
  }
  .card--front .wordmark {
    position: absolute; left: 398px; width: 480px; top: 128px; text-align: center; font-size: 42px;
  }

  .agent-name {
    position: absolute; left: 40px; width: 310px; top: 346px; text-align: center;
    font-family: "Roboto", sans-serif; font-weight: 500; font-size: 35px; color: var(--ink-soft);
    line-height: 1.2;
  }
  .firm {
    position: absolute; left: 40px; width: 310px; top: 402px; text-align: center;
    font-family: "Open Sans", sans-serif; font-weight: 400; font-size: 36px; color: var(--ink);
    line-height: 1.2;
  }

  .contacts { position: absolute; left: 410px; top: 284px; list-style: none; }
  .contacts li {
    display: flex; align-items: center; height: 43px;
    font-family: "Open Sans", sans-serif; font-size: 25px; color: var(--ink-soft);
  }
  .contacts svg { width: 24px; height: 24px; margin-right: 24px; flex: none; }
</style>
</head>
<body>
<main class="canvas">

  <section class="card card--back" aria-label="Card back">
    <div class="brushed"></div>
    <p class="wordmark">Leonard The Realtor</p>
  </section>

  <section class="card card--front" aria-label="Card front">
    <div class="front-top brushed"></div>
    <div class="gold-rule gold-rule--band"></div>
    <div class="gold-rule gold-rule--foot"></div>
    <div class="front-foot brushed"></div>

    <div class="portrait" role="img" aria-label="Portrait photo of the agent in a navy suit"></div>
    <p class="wordmark">Leonard The Realtor</p>

    <h1 class="agent-name">Marisol Vega</h1>
    <p class="firm">Harbor 9</p>

    <ul class="contacts">
      <li>
        <svg viewBox="0 0 24 24" aria-hidden="true"><rect x="2" y="5" width="20" height="14" rx="1" fill="var(--gold)"/><path d="M2 6l10 7 10-7" fill="none" stroke="#fff" stroke-width="1.6"/></svg>
        Info@Leonardtherealtor.com
      </li>
      <li>
        <svg viewBox="0 0 24 24" aria-hidden="true" fill="none" stroke="var(--gold)" stroke-width="1.6"><circle cx="12" cy="12" r="9.5"/><ellipse cx="12" cy="12" rx="4.2" ry="9.5"/><path d="M2.5 12h19M4 7h16M4 17h16"/></svg>
        LeonardtheRealtor.com
      </li>
      <li>
        <svg viewBox="0 0 24 24" aria-hidden="true" fill="none" stroke="var(--gold)" stroke-width="2"><rect x="6.5" y="2" width="11" height="20" rx="1.5"/><path d="M10.5 18.5h3"/></svg>
        206-555-0147
      </li>
      <li>
        <svg viewBox="0 0 24 24" aria-hidden="true" fill="var(--gold)"><rect x="2" y="4" width="5" height="17" rx="1"/><rect x="8" y="9" width="14" height="12" rx="1"/><rect x="10" y="3" width="9" height="5"/><g fill="#fff"><rect x="10.5" y="12" width="2" height="2"/><rect x="14" y="12" width="2" height="2"/><rect x="17.5" y="12" width="2" height="2"/><rect x="10.5" y="16" width="2" height="2"/><rect x="14" y="16" width="2" height="2"/><rect x="17.5" y="16" width="2" height="2"/></g></svg>
        206-555-0193
      </li>
    </ul>
  </section>

</main>
</body>
</html>
```